Optometric Practice needs Initial Photoshop Mockup

We need a graphic design for the homepage of a website for an optometric practice that specializes in vision therapy.

Here's the link to the project folder on Stashvale. I've included photos, example sites, content and instructions.

https://www.stashvale.example/sh/kx7rm2wq8zn41d9/BBQ_LmTyRwoPvXe3NcDrKuWjz

Please feel free to submit any questions about the design. I'll be happy to help guide you in any areas you're uncertain of.

Okay - I've updated the project to payment confirmed. Let's see some designs :) Thanks, Reg

```html
<!DOCTYPE html>
<html lang="en">
<head>
<meta charset="utf-8">
<title>Clearpath Vision Centers – Home</title>
<link href="https://fonts.googleapis.com/css2?family=Arimo:wght@400;700&family=Questrial&display=swap" rel="stylesheet">
<style>
:root{
  --page:#ececec;
  --panel:#ffffff;
  --red:#a80000;
  --red-text:#c00000;
  --nav-line:#7c0000;
  --nav-active:#8c8c8c;
  --heading-blue:#2b3190;
  --footer-blue:#2d4ea2;
  --text:#333333;
  --muted:#666666;
  --btn-blue:#4b57d8;
}
*{box-sizing:border-box;margin:0;padding:0}
html,body{width:968px;height:1200px;overflow:hidden;background:var(--page)}
body{font-family:"Arimo",Arial,sans-serif;color:var(--text);position:relative}
.abs{position:absolute}

/* header */
.call{left:394px;top:32px;font-size:14px;color:#444}
.call .phone{font-size:20px;color:var(--red-text);margin-left:12px;letter-spacing:.5px}
.appt{left:658px;top:11px;width:217px;height:43px;border-radius:6px;background:linear-gradient(#6a74ee,var(--btn-blue));box-shadow:0 2px 3px rgba(0,0,0,.35);color:#fff;display:flex;align-items:center;gap:10px;padding-left:10px}
.appt .label{line-height:15px;font-size:14px}
.appt .label b{font-size:15px}

/* logo + nav */
.logo-box{left:80px;top:62px;width:214px;height:78px;background:var(--panel);display:flex;align-items:center;justify-content:center;gap:8px}
.brand{font-family:"Arimo",Arial,sans-serif;font-weight:700;color:var(--red);font-size:19px;line-height:21px}
.brand-dot{width:14px;height:14px;border-radius:50%;background:var(--heading-blue)}
.nav{left:80px;top:140px;width:214px;height:287px;background:var(--red);list-style:none;padding-top:3px}
.nav li{height:31.5px;line-height:30px;padding-left:14px;color:#fff;font-size:12px;font-weight:700;border-bottom:1px solid var(--nav-line);position:relative}
.nav li.active{background:var(--nav-active);margin-left:2px;padding-left:12px}
.nav li.active::before{content:"";position:absolute;left:-2px;top:10px;border:5px solid transparent;border-left-color:var(--red)}
.nav li:last-child{border-bottom:0}

/* hero */
.hero{left:309px;top:62px;width:578px;height:367px;background:var(--panel)}
.hero-photo{position:absolute;left:6px;top:7px;width:566px;height:354px;background:linear-gradient(110deg,#e9e6e2 0%,#d8d4cf 45%,#bfb6ad 70%,#5a4a48 100%)}
.hero-caption{position:absolute;left:6px;top:305px;width:566px;height:56px;background:rgba(40,40,40,.78);color:#fff;padding:9px 12px}
.hero-caption h2{font-weight:400;font-size:17px;letter-spacing:.2px}
.hero-caption p{font-size:9.5px;margin-top:5px;letter-spacing:-.1px}
.slide-btn{position:absolute;top:12px;width:22px;height:22px;border:1px solid #ddd}
.slide-btn svg{display:block}

/* main panel */
.main{left:80px;top:442px;width:807px;height:572px;background:var(--panel)}
.divider{left:304px;top:442px;width:2px;height:572px;background:#e2e2e2}
.side-title{font-family:"Questrial",sans-serif;font-size:15px;color:#222;letter-spacing:.3px}
.video{left:92px;top:490px;width:190px;height:154px;background:linear-gradient(135deg,#3a2a25,#7a5a4c 50%,#2d2f3f);border:2px solid #222}
.video .play{position:absolute;left:79px;top:61px;width:30px;height:29px;background:rgba(0,0,0,.75)}
.video .bar{position:absolute;left:0;right:0;bottom:0;height:14px;background:#e8e8e8;font-size:6px;color:#333;display:flex;align-items:center;gap:6px;padding:0 5px}
.video .track{flex:1;height:3px;background:#999}
.fb{left:93px;top:690px;width:190px;height:166px;border:1px solid #b9c2d6;background:#fff}
.fb .head{height:15px;background:#edeff4;font-size:7px;color:#555;padding:3px 4px;border-bottom:1px solid #cfd5e2}
.fb .page{display:flex;gap:6px;padding:7px 6px 0}
.fb .avatar{width:30px;height:30px;background:#c9b8aa}
.fb .pname{font-size:8px;font-weight:700;color:#3b5998;line-height:10px}
.fb .like{display:inline-block;margin-top:3px;background:#5b74a8;color:#fff;font-size:7px;padding:1px 5px}
.fb .count{font-size:6.5px;color:#777;padding:8px 6px 4px;line-height:8px}
.fb .grid{display:grid;grid-template-columns:repeat(5,30px);gap:3px;padding:0 6px}
.fb .grid span{height:30px;background:#b8b2ac}
.quote{left:96px;top:898px;width:192px;font-size:10.5px;line-height:16px;color:#333}
.quote .mark{font-family:Georgia,serif;font-size:16px;color:#444;margin-right:4px}
.readmore{left:96px;top:986px;font-size:11px;color:#e25050;font-style:italic}

.welcome{left:328px;top:449px;font-size:24px;color:var(--heading-blue);font-weight:400}
.intro{left:328px;top:489px;width:540px;font-size:10.6px;line-height:17.7px;color:#333}
.intro .thumb{float:left;width:115px;height:83px;margin:2px 15px 4px 0;background:linear-gradient(135deg,#8e9aa6,#c9b6c9 60%,#7b6aa0)}
.provide{left:330px;top:665px;font-size:11px;font-weight:700;color:var(--red-text);letter-spacing:.2px}
.services{left:328px;top:695px;width:500px;list-style:none;font-size:9.7px;line-height:11.3px;color:#222}
.services li{position:relative;padding-left:14px;margin-bottom:16px}
.services li::before{content:"";position:absolute;left:3px;top:3px;width:4px;height:4px;border-radius:50%;background:var(--red-text)}
.services li.short{width:250px}
.svc-photo{left:584px;top:701px;width:182px;height:112px;background:linear-gradient(120deg,#5a4a30,#b09a5a 40%,#d4c27a 70%,#4a5a7a)}

/* footer */
.f-logo{left:94px;top:1080px;width:194px;height:66px;display:flex;align-items:center;gap:8px}
.f-title{font-size:16px;color:var(--footer-blue);font-weight:400}
.social{left:324px;top:1068px;list-style:none;font-size:11px;color:#222}
.social li{display:flex;align-items:center;gap:7px;height:22.6px}
.social .ico{width:17px;height:17px;border-radius:3px}
.addr{left:504px;top:1064px;font-size:10.8px;line-height:17.7px;color:#222}
.field{background:#fff;border:1px solid #c9c9c9;border-radius:3px;left:745px;width:142px}
.send{left:745px;top:1160px;width:55px;height:20px;border:2px solid #6b9fe0;border-radius:10px;background:#fff;color:#4d7fd0;font-size:12px;text-align:center;line-height:16px}
</style>
</head>
<body>

<header>
  <div class="abs call">Call Us Now!<span class="phone">410-555-0142</span></div>
  <div class="abs appt">
    <svg width="24" height="24" viewBox="0 0 24 24" aria-hidden="true"><rect x="2" y="4" width="20" height="18" rx="2" fill="#fff"/><rect x="2" y="4" width="20" height="5" fill="#d33"/><rect x="6" y="2" width="2" height="5" fill="#555"/><rect x="16" y="2" width="2" height="5" fill="#555"/><text x="12" y="19" font-size="8" text-anchor="middle" font-family="Arial" font-weight="700" fill="#222">15</text></svg>
    <div class="label">Request An<br><b>Appointment Now!</b></div>
  </div>
</header>

<div class="abs logo-box"><span class="brand-dot"></span><span class="brand">Clearpath<br>Vision</span></div>
<ul class="abs nav">
  <li>Home</li><li class="active">Meet Us</li><li>New Patients</li><li>Vision &amp; Learning</li><li>Vision Therapy</li><li>Binocular Vision Disorders</li><li>Head Injuries</li><li>Professionals</li><li>Contact Us</li>
</ul>

<section class="abs hero">
  <div class="hero-photo" role="img" aria-label="Optometrist performing an eye examination on a patient at a diagnostic instrument"></div>
  <div class="hero-caption">
    <h2>IMPROVING VISION, CHANGING LIVES</h2>
    <p>HAPPY KIDS, OR A COLLAGE OF THEIR PHOTOS OF KIDS GETTING VISION THERAPY</p>
    <div class="slide-btn" style="left:500px"><svg width="20" height="20"><path d="M12 5 7 10l5 5" stroke="#fff" stroke-width="1.6" fill="none"/></svg></div>
    <div class="slide-btn" style="left:528px"><svg width="20" height="20"><path d="M8 5l5 5-5 5" stroke="#fff" stroke-width="1.6" fill="none"/></svg></div>
  </div>
</section>

<div class="abs main"></div>
<div class="abs divider"></div>

<aside>
  <h3 class="abs side-title" style="left:96px;top:460px">FEATURED VIDEO</h3>
  <div class="abs video" role="img" aria-label="Video still of a presenter speaking to camera">
    <div class="play"><svg width="30" height="29"><path d="M12 9v11l9-5.5z" fill="#fff"/></svg></div>
    <div class="bar"><span>▶</span><span>00:00</span><span class="track"></span><span>00:00</span></div>
  </div>

  <h3 class="abs side-title" style="left:95px;top:664px">SIDE BANNERS</h3>
  <div class="abs fb">
    <div class="head">Find us on Facepage</div>
    <div class="page"><div class="avatar" role="img" aria-label="Profile photo"></div><div><div class="pname">Clearpath: Dr. Daniel Marsh,<br>Developmental Optometrist</div><span class="like">Like</span></div></div>
    <div class="count">155 people like Clearpath: Dr. Daniel Marsh, Developmental Optometrist.</div>
    <div class="grid" role="img" aria-label="Profile photos of page followers"><span></span><span></span><span></span><span></span><span></span><span></span><span></span><span></span><span></span><span></span></div>
  </div>

  <h3 class="abs side-title" style="left:95px;top:874px">SUCCESS STORIES</h3>
  <p class="abs quote"><span class="mark">“</span>Lorem ipsum dolor sit amet, consectetur adipisicing elit, sed eiusmod tempor incididunt ut labore et dolore sunt culpa qui officia deserunt mollit anim id est laborum.</p>
  <div class="abs readmore">Read more....</div>
</aside>

<main>
  <h1 class="abs welcome">Welcome to Clearpath</h1>
  <p class="abs intro"><span class="thumb" role="img" aria-label="Child looking into a vision testing instrument"></span>There are many visual skills critical for reading and learning. Often, a vision problem is misdiagnosed as an attention problem or a learning disability due to similarity of symptoms. Anyone who is struggling with reading, has poor reading comprehension, or just isn't performing to their full potential, should consider scheduling a developmental vision evaluation. To help determine if you or your child should be tested, Do the Checklist on our Vision Quiz page. Dr. Daniel Marsh is a developmental optometrist who specializes in the diagnosis and treatment of vision problems that interfere with reading and learning. He is a member of the National Optometric Society, the Guild of Developmental Vision Practitioners, and a Fellow in the Academy of Clinical Vision Science.</p>
  <h2 class="abs provide">Clearpath Vision Centers and Dr. Daniel Marsh provide:</h2>
  <div class="abs svc-photo" role="img" aria-label="Optometrist working with a young boy during a therapy session"></div>
  <ul class="abs services">
    <li class="short">Comprehensive Eye Examinations for All Ages,</li>
    <li class="short">including Infants and Preschoolers</li>
    <li class="short">Vision Therapy for All Ages</li>
    <li class="short">Treatment for Learning-related Vision Problems</li>
    <li class="short">Sports Vision Correction and/or Improvement</li>
    <li>Free Monthly Seminars. Visit our Facepage page for information about our free monthly seminars on a variety of topics, including: The Hidden Disability - Undiagnosed Vision Problems</li>
    <li>Continuing Education seminars for Optometrists, Occupational Therapists and Physical Therapists. All CE offerings are free and board approved. For CE information and dates, see our success stories, blogs and videos on Binocular Vision Disorders</li>
    <li>Visual Rehabilitation for Patients with Special Needs, such as Developmental Delays or Traumatic Brain Injury (TBI), including Autism, Stroke, Whiplash, CP, MS, etc.</li>
    <li>Treatment for Stress-related Visual Problems, including Blurred Vision, Visual Stress from Reading and Computers, Eye Strain Headaches, and/or Vision-induced Stomachaches or Motion Sickness</li>
  </ul>
</main>

<footer>
  <div class="abs f-logo"><span class="brand-dot"></span><span class="brand" style="font-size:22px;line-height:24px">Clearpath<br>Vision</span></div>

  <h3 class="abs f-title" style="left:324px;top:1038px">Social media</h3>
  <ul class="abs social">
    <li><span class="ico" style="background:#3b5b9b"></span>Follow us Facepage</li>
    <li><span class="ico" style="background:#4fb3e0"></span>Follow us Chirper</li>
    <li><span class="ico" style="background:#1f6fa8"></span>Follow us Linkwork</li>
    <li><span class="ico" style="background:#c0392b"></span>Vidtube</li>
  </ul>

  <h3 class="abs f-title" style="left:506px;top:1038px">Addresses</h3>
  <address class="abs addr" style="font-style:normal">Clearpath Vision Centers<br>Dr. Daniel Marsh<br>48 Linden Ave. Suite 200, Room 3<br>Hollowbrook, MD, 21299<br>Phone: 410-555-0142</address>

  <h3 class="abs f-title" style="left:745px;top:1038px">contact information</h3>
  <div class="abs field" style="top:1063px;height:19px"></div>
  <div class="abs field" style="top:1089px;height:19px"></div>
  <div class="abs field" style="top:1115px;height:39px"></div>
  <div class="abs send">Send</div>
</footer>

</body>
</html>
```